Flyer-Design für ein Montessori Familienzentrum
Super Zusammenarbeit :) Meine Wünsche und Ideen wurden sehr passend und schnell umgesetzt und miteinbezogen in das Design.
Zielgruppe
Wir sind ein Montessori Familienzentrum mit folgendem Angebot:
- Montessori Eltern-Kind-Gruppen für Babys ab 8 Wochen - 4 Jahren
- Montessori Coaching
- Stoffwindel- und Windelfrei Beratung
- Beratung zur Babygeleiteten Beikost
- Workshops für Eltern
Aufgabenstellung
Schlicht, Informativ, Überblick über die Angebote

```html
<!DOCTYPE html>
<html lang="de">
<head>
<meta charset="utf-8">
<title>Waldspatz – Montessori Eltern-Kind-Kurse Flyer</title>
<link href="https://fonts.googleapis.com/css2?family=Playfair+Display:wght@400;700&family=Jost:ital,wght@0,300;0,400;0,500;1,300;1,400&family=Exo+2:ital,wght@1,800&family=Great+Vibes&display=swap" rel="stylesheet">
<style>
:root{
  --green:#3f6b2c;
  --orange:#e6762c;
  --text:#555;
  --heading:#3d3d3d;
  --paper:#ffffff;
  --band:#f1f1f1;
  --stage:#dcdcdc;
}
*{margin:0;padding:0;box-sizing:border-box}
html,body{width:1200px;height:1200px;overflow:hidden;background:var(--stage)}
body{position:relative;font-family:"Jost",sans-serif;color:var(--text)}
.page{position:absolute;width:580px;height:580px;background:var(--paper);overflow:hidden}
.spread{position:absolute;left:10px;top:10px;width:1180px;height:580px}
.spread .page{top:0}
.page--inner-left{left:0}
.page--inner-right{left:590px}
.page--cover{left:10px;top:610px}
.page--back{left:610px;top:610px}
.abs{position:absolute}
.bands{position:absolute;inset:0}
.photo{position:absolute}

/* cover */
.brand{position:absolute;left:36px;top:52px;display:flex;align-items:center;gap:8px;font-family:"Jost",sans-serif;font-weight:500;font-size:20px;color:var(--green)}
.brand__dot{width:14px;height:14px;border-radius:50%;background:var(--green)}
.cover-title{position:absolute;left:76px;top:408px;font-family:"Playfair Display",serif;color:var(--green);line-height:1}
.cover-title__main{font-size:37px;font-weight:700;letter-spacing:.5px}
.cover-title__sub{font-size:28px;font-weight:400;margin-top:2px}
.cover-tagline{position:absolute;left:78px;top:486px;font-size:11px;letter-spacing:1.8px;color:#666;font-weight:400}
.cover-age{position:absolute;left:290px;top:511px;font-size:11px;letter-spacing:1.8px;color:var(--orange)}
.cover-footer{position:absolute;left:78px;top:558px;display:flex;gap:20px;font-size:8px;letter-spacing:1.2px;color:#666}

/* shared inner */
.headline{font-family:"Exo 2",sans-serif;font-style:italic;font-weight:800;color:var(--orange);line-height:1}
.headline-sub{font-family:"Jost",sans-serif;font-style:italic;font-weight:300;color:#444}
.sec-title{font-family:"Jost",sans-serif;font-weight:400;font-size:18px;color:var(--heading);text-transform:uppercase;line-height:1}
.sec-title--green{color:var(--green)}
.sec-kicker{font-style:italic;font-weight:300;font-size:12px;color:var(--orange);line-height:1.2}
.body{font-size:9px;line-height:1.45;font-weight:300;color:#555;text-align:justify}

/* back */
.intro{position:absolute;left:26px;top:14px;width:296px;font-size:9px;line-height:1.45;font-weight:300;color:#555;text-align:justify}
.signature{position:absolute;left:196px;top:222px;font-family:"Great Vibes",cursive;font-size:24px;color:#444}
.person{position:absolute;left:80px;top:262px;font-size:21px;font-weight:300;color:#444;letter-spacing:.5px}
.credentials{position:absolute;left:130px;top:296px;width:175px;font-size:9px;line-height:1.65;font-style:italic;font-weight:300;color:#555}
.offers{position:absolute;left:16px;top:386px;font-size:23px}
.offer{position:absolute;top:422px}
.offer__title{font-style:italic;font-weight:300;font-size:14px;color:#444;line-height:1.25}
.offer ul{list-style:none;margin-top:4px;padding-left:22px;font-size:9px;line-height:1.5;font-weight:300;color:#555}
.offer li::before{content:"• "}
</style>
</head>
<body>

<!-- inner spread -->
<section class="spread">
  <article class="page page--inner-left">
    <svg class="bands" viewBox="0 0 580 580" aria-hidden="true">
      <polygon points="0,300 580,90 580,240 0,470" fill="var(--band)"/>
    </svg>
    <svg class="photo" style="left:340px;top:0" width="250" height="400" viewBox="0 0 250 400" role="img" aria-label="Foto: Mutter mit Baby im Arm im herbstlichen Park">
      <defs><linearGradient id="gMother" x1="0" y1="0" x2="1" y2="1"><stop offset="0" stop-color="#b98f63"/><stop offset=".55" stop-color="#8e4a2c"/><stop offset="1" stop-color="#5b3a2a"/></linearGradient></defs>
      <path d="M60 0 H250 V400 H140 C60 400 0 340 8 260 C14 190 60 160 40 100 C28 60 30 20 60 0 Z" fill="url(#gMother)"/>
    </svg>
    <svg class="photo" style="left:0;top:395px" width="240" height="185" viewBox="0 0 240 185" role="img" aria-label="Foto: Kinder feiern ein Gartenfest am gedeckten Tisch">
      <defs><linearGradient id="gParty" x1="0" y1="0" x2="0" y2="1"><stop offset="0" stop-color="#8fbf5a"/><stop offset=".5" stop-color="#d99ab0"/><stop offset="1" stop-color="#c9a15c"/></linearGradient></defs>
      <path d="M0 10 C60 -6 150 -4 200 30 C240 60 245 130 225 185 H0 Z" fill="url(#gParty)"/>
    </svg>

    <h1 class="headline abs" style="left:22px;top:14px;font-size:26px">Spielgruppen für Babys</h1>
    <p class="headline-sub abs" style="left:180px;top:42px;font-size:15px">Ab 8 Wochen – 4 Jahre</p>

    <h2 class="sec-title abs" style="left:22px;top:84px">Was ist Montessori?</h2>
    <p class="sec-kicker abs" style="left:96px;top:102px">Informationen zum pädagogischen Konzept</p>
    <p class="body abs" style="left:22px;top:124px;width:305px">In den Gruppenstunden liegt der Schwerpunkt auf der Beobachtung seines eigenen Kindes und der Eltern-Kind-Beziehung. Jedes Kind gestaltet seine Zeit ganz individuell nach seinen Bedürfnissen. Jede Gruppe hat einen individuell gestalteten Gruppenraum mit Montessori Material aus der Altersgruppe 0-3 Jahren sowie 3-6 Jahren.</p>

    <h2 class="sec-title abs" style="left:22px;top:206px">Umsetzung Zuhause</h2>
    <p class="sec-kicker abs" style="left:190px;top:224px">Anleitung der Eltern</p>
    <p class="body abs" style="left:22px;top:244px;width:275px">Zu jedem Thema bekommen die Eltern Unterstützung und Hilfestellung zur Umsetzung zu Hause. Im Elternportal der Website finden sie außerdem zusätzliche Tipps und Tricks.</p>

    <h2 class="sec-title abs" style="left:22px;top:306px">Familien-Events</h2>
    <p class="sec-kicker abs" style="left:86px;top:324px">Austausch und Vernetzung</p>
    <p class="body abs" style="left:22px;top:344px;width:320px">1x pro Kursblock findet ein Eltern-Event wie z.B. Eltern-Coaching, Sommerfest, Martinsumzug, etc. statt. Die Eltern können sich mit Teilnehmern aus anderen Kursen austauschen.</p>

    <h2 class="headline abs" style="left:208px;top:410px;font-size:24px">Montessori Coaching für Zuhause</h2>
    <p class="headline-sub abs" style="left:393px;top:438px;font-size:15px">Ab Babyalter - Preschool Alter</p>
    <p class="body abs" style="left:270px;top:474px;width:300px">Wir gestalten zusammen Euer individuelles Zuhause nach den Prinzipien der Montessori Pädagogik.</p>
    <p class="abs" style="left:270px;top:508px;font-size:9px;font-weight:400;color:#555">WIE LÄUFT EIN MONTESSORI COACHING AB?</p>
    <p class="body abs" style="left:270px;top:522px;width:300px">Das Coaching besteht aus 3 Hausbesuchen, die jeweils ca. 2 Stunden dauern und sich über einen Zeitraum von 6-8 Wochen erstrecken.</p>
  </article>

  <article class="page page--inner-right">
    <svg class="bands" viewBox="0 0 580 580" aria-hidden="true">
      <polygon points="0,380 580,180 580,330 0,530" fill="var(--band)"/>
    </svg>
    <svg class="photo" style="left:270px;top:0" width="310" height="580" viewBox="0 0 310 580" role="img" aria-label="Fotos: Baby auf einer Decke, krabbelndes Kleinkind, Montessori Regal mit Geschirr und Globus">
      <defs>
        <linearGradient id="gBaby" x1="0" y1="0" x2="1" y2="1"><stop offset="0" stop-color="#f4efee"/><stop offset="1" stop-color="#d9cfcf"/></linearGradient>
        <linearGradient id="gCrawl" x1="0" y1="0" x2="1" y2="1"><stop offset="0" stop-color="#b8c7c9"/><stop offset="1" stop-color="#e7dccd"/></linearGradient>
        <linearGradient id="gShelf" x1="0" y1="0" x2="1" y2="1"><stop offset="0" stop-color="#e6d8c3"/><stop offset="1" stop-color="#c9b79b"/></linearGradient>
      </defs>
      <path d="M40 0 H310 V142 H20 C8 100 20 40 40 0 Z" fill="url(#gBaby)"/>
      <path d="M20 146 H310 V336 H40 C10 290 0 210 20 146 Z" fill="url(#gCrawl)"/>
      <path d="M42 340 H310 V580 H200 C190 520 170 490 140 470 C100 440 60 420 42 340 Z" fill="url(#gShelf)"/>
    </svg>

    <h1 class="headline abs" style="left:22px;top:14px;font-size:26px">Gruppeneinteilung</h1>

    <h2 class="sec-title sec-title--green abs" style="left:22px;top:60px">Baby Kurse</h2>
    <p class="sec-kicker abs" style="left:68px;top:76px">ab 8 Wochen bis 6 Monate</p>
    <p class="body abs" style="left:22px;top:102px;width:230px">Im Baby Kurs lernen die Teilnehmer unter anderem die verschiedenen Montessori Mobiles kennen. Wir sprechen über Themen wie z.B.: Ernährung, bedürfnisorientiertes Wickeln, Eingewöhnung in die KITA und noch vieles mehr.</p>

    <h2 class="sec-title sec-title--green abs" style="left:22px;top:202px">Crawler Kurse</h2>
    <p class="sec-kicker abs" style="left:68px;top:218px">ab 6 Monaten bis ca.15 Monate</p>
    <p class="body abs" style="left:22px;top:244px;width:245px">Im Crawler Kurs findet eine gemeinsame Brotzeit nach BLW statt. Ein Montessori Spiegel mit integrierter Pull-up-Stange lädt die Kinder zum Hochziehen ein. Die Kinder finden außerdem Montessori Material für ihre Altersgruppe.</p>

    <h2 class="sec-title sec-title--green abs" style="left:22px;top:344px">Toddler Kurse</h2>
    <p class="sec-kicker abs" style="left:66px;top:360px">ab ca. 15 Monaten bis max. 36 Monate</p>
    <p class="body abs" style="left:22px;top:386px;width:300px">In den Toddler Kursen liegt der Schwerpunkt auf den Dingen des täglichen Lebens und auf der Entwicklung zur Selbständigkeit. So können sie sich selbst Essen zu bereiten, sich selbst ein Glas Wasser einschenken und noch vieles mehr.</p>

    <h2 class="sec-title sec-title--green abs" style="left:22px;top:464px">Prescooler Kurse</h2>
    <p class="sec-kicker abs" style="left:68px;top:480px">ab 2 Jahren bis max. 4 Jahre</p>
    <p class="body abs" style="left:22px;top:504px;width:380px">Im Preschooler Kurs haben die Kinder neben den Übungen des täglichen Lebens noch zusätzlich die Möglichkeit, erste Erfahrungen mit Buchstaben und Zahlen, sowie mit Geografie-Material zu machen.</p>

    <p class="abs" style="left:22px;top:560px;font-size:9.5px;letter-spacing:1px;font-weight:400;color:#444">MONTESSORI PÄDAGOGIK FÜR BABYS UND KLEINKINDER</p>
  </article>
</section>

<!-- cover -->
<article class="page page--cover">
  <svg class="bands" viewBox="0 0 580 580" aria-hidden="true">
    <polygon points="0,0 580,0 580,80 0,250" fill="var(--band)"/>
    <polygon points="0,370 580,190 580,320 0,500" fill="var(--band)"/>
  </svg>
  <div class="brand"><span class="brand__dot"></span>Waldspatz</div>
  <svg class="photo" style="left:140px;top:22px" width="390" height="400" viewBox="0 0 390 400" role="img" aria-label="Foto: lachende Mutter sitzt hinter krabbelndem Baby, das nach einem bunten Ball greift">
    <defs><radialGradient id="gCover" cx=".5" cy=".45" r=".6"><stop offset="0" stop-color="#e9a08c"/><stop offset=".55" stop-color="#a89f8c"/><stop offset="1" stop-color="#f6f6f6" stop-opacity="0"/></radialGradient></defs>
    <ellipse cx="195" cy="210" rx="195" ry="200" fill="url(#gCover)"/>
  </svg>
  <div class="cover-title">
    <div class="cover-title__main">MONTESSORI</div>
    <div class="cover-title__sub">Eltern-Kind-Kurse</div>
  </div>
  <p class="cover-tagline">MONTESSORI PÄDAGOGIK FÜR BABYS UND KLEINKINDER</p>
  <p class="cover-age">AB 8 WOCHEN BIS 4 JAHRE</p>
  <div class="cover-footer">
    <span>INFO@WALDSPATZ.DE</span><span>WWW. WALDSPATZ.DE</span><span>WALDSPATZ</span><span>WALDSPATZ</span>
  </div>
</article>

<!-- back -->
<article class="page page--back">
  <svg class="bands" viewBox="0 0 580 580" aria-hidden="true">
    <polygon points="0,300 580,80 580,230 0,420" fill="var(--band)"/>
  </svg>
  <svg class="photo" style="left:325px;top:0" width="255" height="415" viewBox="0 0 255 415" role="img" aria-label="Foto: Familie im Feld, Kind auf den Schultern des Vaters, Mutter im Vordergrund">
    <defs><linearGradient id="gFamily" x1="0" y1="0" x2="0" y2="1"><stop offset="0" stop-color="#c9bfcf"/><stop offset=".45" stop-color="#a8784e"/><stop offset="1" stop-color="#6e5038"/></linearGradient></defs>
    <path d="M60 0 H255 V340 C240 395 190 415 135 415 C55 415 0 360 2 280 C4 200 35 150 40 90 C44 45 48 20 60 0 Z" fill="url(#gFamily)"/>
  </svg>
  <p class="intro">Hallo,<br>mein Name ist Theresa, ich bin Jahrgang 1994, verheiratet und wohne mit meiner Familie in Auenfeld. Ich bin staatlich anerkannte Erzieherin und habe nach meiner Ausbildungszeit zunächst ein Jahr in Amerika gelebt und gearbeitet und danach in einer normalen und einer integrativen Kinderkrippe. Den Waldspatz habe ich im September 2020 gegründet und seit September 2021 hat das Kurskonzept einen Montessori Schwerpunkt.<br>Neben meiner Fortbildung zur Montessori Spielgruppenleiterin bei Karin Albers und zahlreichen Fortbildungen zum Montessori Kinderhaus Material, mache ich derzeit noch zusätzlich mein Montessori Diplom für Kleinkinder an der Montessori Akademie. Ich bin außerdem zertifizierte Stoffwindelberaterin, Windelfrei Coach und Fachkraft für Babygeleitet Beikost (BLW).<br>Ich freue mich Euch in einem meiner Kurse kennenzulernen.</p>
  <p class="signature">Eure Theresa</p>
  <h2 class="person">THERESA LINDNER</h2>
  <p class="credentials">Staatlich anerkannte Erzieherin -<br>Diplom Montessori Pädagogin i.A.<br>zertifizierte Stoffwindelberaterin /<br>Abhalte- und Windelfrei Coach,<br>Fachkraft für Babygeleitete Beikost</p>
  <h2 class="headline offers">Weiter Beratungsangebote:</h2>
  <div class="offer" style="left:20px;width:265px">
    <p class="offer__title">Stoffwindel– und Windelfrei-Beratung:</p>
    <p class="body" style="margin-top:3px">Für alle Eltern, die sich für das Thema Stoffwindeln und Abhalten interessierenund gern mehr darüber erfahren möchten. Auch für (Stoff)-Eltern, die Probleme haben oder etwas Neues ausprobieren wollen.</p>
    <ul><li>Einzel- Paarberatung</li><li>Workshops</li><li>Stoffwindelparty</li><li>Problemanalysen</li><li>Miet- und Testpakete (ab Geburt – Trocken werden)</li></ul>
  </div>
  <div class="offer" style="left:302px;width:265px">
    <p class="offer__title">Beratung rund ums Thema:<br>Babygeleitete Beikost</p>
    <p class="body" style="margin-top:3px">Du möchtest wissen, was genau BLW ist und wie man es am besten umsetzt? Oder setzt es schon um, kommst aber nicht weiter? Dann ist eine individuelle Beratung genau das Richtige!</p>
    <ul><li>Einzelberatungen</li><li>Workshops</li></ul>
  </div>
</article>

</body>
</html>
```